Quarvine, Cosmetic skin care line

I am not looking to change my logo quarvine on the label just want someone to design a different label I want it to be very classy as it is already just want something different. My product target classier people and people with higher income and for woman and men but mostly women. Looking to keep the label background black

Target Market(s)

Classier and higer income women/men mostly women

Industry/Entity Type

Cosmetics

• I don't really know

Colors

Designer to choose colors to be used in the design.

Requirements
Must have
• It must keep the same quarvine logo and the same matte black background color
Nice to have
• I want a different layout and maybe different fonts for the label
Should not have

```html
<!DOCTYPE html>
<html lang="en">
<head>
<meta charset="UTF-8">
<title>Quarvine Eye Corrector Serum – Labels</title>
<link href="https://fonts.googleapis.com/css2?family=Montserrat:wght@400;500;700&display=swap" rel="stylesheet">
<style>
  :root {
    --backdrop: #1c0404;
    --label-black: #0d0d0d;
    --label-white: #f4f4f4;
    --ink-dark: #1a1a1a;
    --ink-light: #ffffff;
    --rule: #bdbdbd;
  }
  * { margin: 0; padding: 0; box-sizing: border-box; }
  html, body {
    width: 1126px; height: 1200px; overflow: hidden;
    background: var(--backdrop);
    font-family: "Montserrat", sans-serif;
  }
  .canvas { position: relative; width: 1126px; height: 1200px; }

  /* Shared name tab */
  .logo-tab {
    position: absolute; left: 50%; transform: translateX(-50%);
    background: var(--label-white);
    border-radius: 0 0 16px 16px;
    display: flex; align-items: center; justify-content: center;
    color: var(--ink-dark);
  }
  .logo-name { font-weight: 500; letter-spacing: 0.06em; line-height: 1; }

  .product-title { text-align: center; color: var(--ink-light); }
  .title-kicker { font-weight: 500; letter-spacing: 0.16em; }
  .title-main { font-weight: 700; letter-spacing: 0.03em; line-height: 1; }
  .title-rule { height: 1px; background: var(--rule); margin: 0 auto; }

  /* Jar wrap label (flattened) */
  .jar-label {
    position: absolute; left: 63px; top: 110px;
    width: 1000px; height: 270px;
    background: var(--label-black);
  }
  .jar-label .logo-tab { top: 0; width: 150px; height: 106px; }
  .jar-label .logo-name { font-size: 22px; }
  .jar-label .product-title { position: absolute; left: 50%; top: 124px; transform: translateX(-50%); width: 260px; }
  .jar-label .title-kicker { font-size: 19px; }
  .jar-label .title-rule { width: 200px; margin-top: 5px; margin-bottom: 6px; }
  .jar-label .title-main { font-size: 54px; }
  .jar-label .title-sub { font-size: 17px; font-weight: 700; margin-top: 4px; }
  .jar-copy {
    position: absolute; top: 58px; width: 250px;
    font-size: 13px; line-height: 1.45; color: var(--ink-light);
  }
  .jar-copy.left { left: 70px; }
  .jar-copy.right { right: 70px; text-align: center; }

  /* Bottle label (flattened) */
  .bottle-label {
    position: absolute; left: 398px; top: 500px;
    width: 330px; height: 560px;
    background: var(--label-black);
  }
  .bottle-label .logo-tab { top: 0; width: 220px; height: 150px; border-radius: 0 0 20px 20px; }
  .bottle-label .logo-name { font-size: 32px; }
  .bottle-label .product-title { position: absolute; left: 0; right: 0; top: 200px; }
  .bottle-label .title-kicker { font-size: 22px; line-height: 1.4; }
  .bottle-label .title-rule { width: 240px; margin-top: 8px; margin-bottom: 10px; }
  .bottle-label .title-main { font-size: 68px; }
  .bottle-label .title-rule.lower { margin-top: 10px; margin-bottom: 8px; }
  .bottle-label .title-sub { font-size: 22px; font-weight: 400; letter-spacing: 0.04em; line-height: 1.4; }
  .volume-tab {
    position: absolute; left: 50%; bottom: 0; transform: translateX(-50%);
    width: 240px; height: 70px;
    background: var(--label-white);
    border-radius: 20px 20px 0 0;
    display: flex; align-items: center; justify-content: center;
    font-size: 16px; color: var(--ink-dark);
  }
</style>
</head>
<body>
<main class="canvas">

  <section class="jar-label" aria-label="Jar label">
    <div class="logo-tab">
      <span class="logo-name">QUARVINE</span>
    </div>
    <p class="jar-copy left">A silky serum for the delicate eye area. Smooths fine lines, softens puffiness and brightens tired skin with daily use.</p>
    <div class="product-title">
      <p class="title-kicker">EYE CORRECTOR</p>
      <div class="title-rule"></div>
      <p class="title-main">SERUM</p>
      <div class="title-rule"></div>
      <p class="title-sub">with triple peptides</p>
    </div>
    <p class="jar-copy right">Apply a small amount morning and night. Pat gently around the eyes until absorbed. For external use only.</p>
  </section>

  <section class="bottle-label" aria-label="Bottle label">
    <div class="logo-tab">
      <span class="logo-name">QUARVINE</span>
    </div>
    <div class="product-title">
      <p class="title-kicker">EYE<br>CORRECTOR</p>
      <div class="title-rule"></div>
      <p class="title-main">SERUM</p>
      <div class="title-rule lower"></div>
      <p class="title-sub">WITH<br>TRIPLE PEPTIDES</p>
    </div>
    <div class="volume-tab">5ml | 0.03oz</div>
  </section>

</main>
</body>
</html>
```